Tenth Annual Silverwave Ivory Costume Soiree to Benefit Harborlight Capital Circle Trust

Date: 2 February 2024
Location: The Corvane Palmridge Coralbay Shore Resort & Spa
Time: Doors open 5:00pm
Attire: White Elegance (a variety of masks will be available at the extravaganza)

Target Market(s)

Early to mid career men and women (aged 25-40)

Industry/Entity Type

Financial Services / Asset Management

Font styles to use
Serif

Colors
0054AA
0677BA
7BADD7
CADEEF
E8F1F8
00AB8E
00BBA5
67D7C9
C6EFE9
E9F9F6
59FF00
82FF00
B8FF75
E3FFCB
F4FFEA

Requirements
Must have
• Masquerade images. The event is being held on the beach in the Caribbean.

```html
<!DOCTYPE html>
<html lang="en">
<head>
<meta charset="utf-8">
<title>Silverwave Ivory Costume Soiree</title>
<link rel="stylesheet" href="https://fonts.googleapis.com/css2?family=Cinzel:wght@400;600;700;900&family=Great+Vibes&family=Poppins:wght@400;500;600;700;800&display=swap">
<style>
  :root {
    --backdrop: #ececec;
    --cream-light: #fdf9f0;
    --cream: #f6eedb;
    --cream-deep: #efe2c3;
    --gold-light: #f3d27a;
    --gold: #d29a2a;
    --gold-deep: #a86f17;
    --bronze: #8a5a12;
    --maroon: #561012;
    --rust: #8c3a0c;
    --ink: #1c1410;
  }
  * { margin: 0; padding: 0; box-sizing: border-box; }
  html, body { width: 1200px; height: 2400px; overflow: hidden; }
  body { background: var(--backdrop); position: relative; font-family: "Poppins", sans-serif; }

  .flyer {
    position: absolute; left: 0; top: 423px; width: 1200px; height: 1553px; overflow: hidden;
    background: radial-gradient(ellipse at 50% 40%, var(--cream-light) 0%, var(--cream) 60%, var(--cream-deep) 100%);
  }
  .abs { position: absolute; }
  .center-x { left: 0; width: 100%; text-align: center; }

  .banner-ribbon {
    left: 284px; top: 54px; width: 627px; height: 153px;
    background: linear-gradient(180deg, var(--gold-light) 0%, var(--gold) 50%, var(--gold-deep) 100%);
    border-radius: 18px; opacity: .9;
  }
  .banner-year { top: 68px; font-family: "Poppins", sans-serif; font-weight: 700; font-size: 56px; color: var(--ink); line-height: 1; }
  .banner-year sup { font-size: 30px; vertical-align: 22px; }
  .banner-name { top: 140px; font-family: "Cinzel", serif; font-weight: 600; font-size: 38px; letter-spacing: 8px; color: var(--maroon); line-height: 1; }

  .mask-art {
    left: 0; top: 458px; width: 1200px; height: 536px;
    background: radial-gradient(ellipse 55% 50% at 42% 52%, #f0c24e 0%, #d39a2c 45%, rgba(200,140,40,.55) 70%, rgba(246,238,219,0) 100%);
  }

  .title-main { top: 218px; font-family: "Cinzel", serif; font-weight: 900; font-size: 190px; line-height: 1; color: var(--gold-deep); letter-spacing: 2px; }
  .title-sub { top: 372px; font-family: "Cinzel", serif; font-weight: 400; font-size: 128px; line-height: 1; color: var(--maroon); }
  .title-script { left: 610px; top: 470px; width: 380px; text-align: center; font-family: "Great Vibes", cursive; font-size: 150px; line-height: 1; color: var(--gold); }

  .date-line { top: 1038px; font-family: "Poppins", sans-serif; font-weight: 800; font-size: 72px; line-height: 1.1; color: var(--gold-deep); word-spacing: 10px; }
  .date-line sup { font-size: 40px; vertical-align: 26px; }
  .date-line .sep { font-weight: 400; margin: 0 22px; }
  .doors { top: 1128px; font-family: "Cinzel", serif; font-weight: 700; font-size: 58px; line-height: 1; color: var(--ink); }

  .venue-rule { left: 76px; width: 1044px; height: 3px; background: var(--gold-deep); }
  .venue-rule.top { top: 1207px; }
  .venue-rule.bottom { top: 1264px; }
  .venue { top: 1218px; font-weight: 700; font-size: 28px; line-height: 36px; color: var(--rust); display: flex; justify-content: center; align-items: center; gap: 14px; }
  .venue svg { width: 20px; height: 28px; }

  .attire {
    left: 96px; top: 1294px; width: 978px; height: 54px;
    border: 2px solid var(--gold); border-radius: 10px; display: flex; align-items: center; overflow: hidden;
  }
  .attire-label {
    flex: 0 0 124px; height: 100%; display: flex; align-items: center; justify-content: center;
    background: linear-gradient(180deg, var(--gold-light), var(--gold-deep));
    font-weight: 700; font-size: 25px; letter-spacing: .5px; color: var(--ink);
  }
  .attire-text {
    flex: 1; padding: 0 14px 0 18px; font-size: 19.5px; letter-spacing: -.2px;
    color: var(--ink); white-space: nowrap;
  }
  .attire-text strong { font-weight: 700; }

  .host { top: 1396px; display: flex; justify-content: center; align-items: center; gap: 18px; }
  .host-dot { width: 64px; height: 64px; border-radius: 50%; background: var(--gold-deep); }
  .host-name { font-weight: 600; font-size: 34px; color: var(--maroon); }
</style>
</head>
<body>
  <main class="flyer">
    <div class="abs banner-ribbon" role="img" aria-label="Gold satin ribbon banner"></div>
    <div class="abs center-x banner-year">10<sup>th</sup> Annual</div>
    <div class="abs center-x banner-name">SILVERWAVE</div>

    <div class="abs mask-art" role="img" aria-label="Gold masquerade mask with satin ribbon, glitter ornament and gold feathers"></div>

    <h1 class="abs center-x title-main">IVORY</h1>
    <div class="abs center-x title-sub">COSTUME</div>
    <div class="abs title-script">Soiree</div>

    <div class="abs center-x date-line">2<sup>ND</sup><span class="sep">|</span>FEBRUARY<span class="sep">|</span>2024</div>
    <div class="abs center-x doors">DOORS OPEN AT 5:00PM</div>

    <div class="abs venue-rule top"></div>
    <div class="abs center-x venue">
      <svg viewBox="0 0 20 28" aria-hidden="true"><path d="M10 0C4.5 0 0 4.4 0 9.8 0 17 10 28 10 28s10-11 10-18.2C20 4.4 15.5 0 10 0zm0 14a4.2 4.2 0 1 1 0-8.4 4.2 4.2 0 0 1 0 8.4z" fill="#8c3a0c"/></svg>
      THE CORVANE PALMRIDGE CORALBAY SHORE RESORT &amp; SPA
    </div>
    <div class="abs venue-rule bottom"></div>

    <div class="abs attire">
      <div class="attire-label">ATTIRE</div>
      <div class="attire-text"><strong>WHITE ELEGANCE</strong> (A variety of masks will be available at the extravaganza)</div>
    </div>

    <div class="abs center-x host">
      <span class="host-dot"></span>
      <span class="host-name">Harborlight Capital Circle Trust</span>
    </div>
  </main>
</body>
</html>
```